Women's Clothing / Pip & Tansy's
I'd prefer to have the logo centered at the top of the letterhead and have the address, etc. listed on the bottom. Also, I'm not fond of the little icons that indicate address, phone, email, web. Maybe an envelope with just the logo on the front and the return address on the flap? I think they all look really busy with the big logo in the corner and the address on the bottom. It's something I won't use often, so simple is good.
I really like the front of the business card in #4 and the back of the card in purple. More feedback later on the rest. Thanks for all of the options so far!
Cute design, thanks! What would it look like if the back was purple and the logo was white?

```html
<!DOCTYPE html>
<html lang="en">
<head>
<meta charset="utf-8">
<title>Pip &amp; Tansy's – Stationery Design</title>
<link rel="stylesheet" href="https://fonts.googleapis.com/css2?family=Raleway:wght@400;600&family=Cinzel:wght@400&display=swap">
<style>
  :root {
    --plum: #8c2f6f;
    --plum-soft: #eedfe8;
    --pink: #d9579a;
    --paper: #ffffff;
    --ink: #5a5a5a;
    --backdrop: #6f7378;
    --title: #f2f2f2;
  }
  * { box-sizing: border-box; margin: 0; padding: 0; }
  html, body { width: 1200px; height: 794px; overflow: hidden; }
  body {
    position: relative;
    background: var(--backdrop);
    font-family: "Raleway", Arial, sans-serif;
    color: var(--ink);
  }
  .board-title {
    position: absolute; top: 26px; left: 0; width: 1200px;
    text-align: center;
    font-family: "Cinzel", Georgia, serif;
    font-size: 30px; letter-spacing: 1px; color: var(--title);
  }
  .piece { position: absolute; background: var(--paper); box-shadow: 0 2px 6px rgba(0,0,0,.35); overflow: hidden; }
  .brand { font-weight: 600; color: var(--plum); white-space: nowrap; }
  .tagline { font-size: 6px; letter-spacing: 1px; color: var(--pink); text-transform: uppercase; }
  .mark { position: absolute; border-radius: 50%; background: var(--plum); }

  /* business cards */
  .card { left: 125px; width: 230px; height: 128px; }
  .card-front { top: 240px; }
  .card-front .brand { position: absolute; left: 14px; top: 12px; font-size: 14px; }
  .card-front .tagline { position: absolute; left: 14px; top: 32px; }
  .card-front .mark { left: -38px; top: 48px; width: 96px; height: 96px; }
  .card-contact { position: absolute; left: 124px; top: 46px; font-size: 6px; line-height: 1.55; }
  .card-contact .person { font-size: 8px; font-weight: 600; color: var(--plum); }
  .card-contact .role { color: var(--pink); margin-bottom: 6px; }
  .card-web { position: absolute; right: 12px; bottom: 8px; font-size: 6px; color: var(--pink); }

  .card-back-light { top: 390px; }
  .card-back-plum { top: 542px; background: var(--plum); }
  .card-center { position: absolute; inset: 0; display: flex; align-items: center; justify-content: center; gap: 8px; }
  .card-center .dot { width: 40px; height: 40px; border-radius: 50%; background: var(--plum); }
  .card-center .brand { font-size: 15px; }
  .card-back-plum .dot { background: none; border: 2px solid var(--paper); }
  .card-back-plum .brand { color: var(--paper); }

  /* letterhead */
  .letterhead { left: 367px; top: 173px; width: 427px; height: 552px; }
  .letterhead-head { position: absolute; top: 26px; left: 0; width: 100%; text-align: center; }
  .letterhead-head .dot { width: 40px; height: 40px; border-radius: 50%; background: var(--plum); margin: 0 auto 6px; }
  .letterhead-head .brand { font-size: 16px; }
  .letterhead-head .tagline { margin-top: 3px; }
  .letterhead-fade { position: absolute; left: -2px; top: 355px; width: 220px; height: 220px; border-radius: 50%; background: var(--plum-soft); }
  .letterhead-foot { position: absolute; bottom: 14px; left: 0; width: 100%; text-align: center; font-size: 6.5px; letter-spacing: .3px; }

  /* envelopes */
  .envelope-back { left: 600px; top: 380px; width: 462px; height: 144px; }
  .envelope-back svg { position: absolute; inset: 0; }
  .flap-return { position: absolute; top: 10px; left: 0; width: 100%; text-align: center; font-size: 6px; letter-spacing: .5px; }
  .envelope-back .mark { left: 22px; top: 52px; width: 24px; height: 24px; }
  .envelope-back .brand { position: absolute; left: 52px; top: 58px; font-size: 11px; }

  .envelope-front { left: 677px; top: 456px; width: 385px; height: 144px; }
  .envelope-front .mark { left: 20px; top: 16px; width: 26px; height: 26px; }
  .envelope-front .brand { position: absolute; left: 52px; top: 22px; font-size: 12px; }
  .envelope-front .tagline { position: absolute; left: 52px; top: 40px; }
</style>
</head>
<body>
  <h1 class="board-title">Stationary Design</h1>

  <section class="piece card card-front">
    <div class="brand">Pip &amp; Tansy's</div>
    <div class="tagline">clothing &amp; accessories</div>
    <span class="mark"></span>
    <div class="card-contact">
      <div class="person">Corbel Wrenx</div>
      <div class="role">Owner</div>
      <div>14 Fernhollow Lane</div>
      <div>Larkmoor, MN 55011</div>
      <div>P 612.555.0147</div>
      <div>E hello@pipandtansys.com</div>
    </div>
    <div class="card-web">www.pipandtansys.com</div>
  </section>

  <section class="piece card card-back-light">
    <div class="card-center"><span class="dot"></span><span class="brand">Pip &amp; Tansy's</span></div>
  </section>

  <section class="piece card card-back-plum">
    <div class="card-center"><span class="dot"></span><span class="brand">Pip &amp; Tansy's</span></div>
  </section>

  <section class="piece letterhead">
    <span class="letterhead-fade"></span>
    <header class="letterhead-head">
      <div class="dot"></div>
      <div class="brand">Pip &amp; Tansy's</div>
      <div class="tagline">clothing &amp; accessories</div>
    </header>
    <footer class="letterhead-foot">14 Fernhollow Lane, Larkmoor, MN 55011 &nbsp;|&nbsp; P 612.555.0147 &nbsp;|&nbsp; hello@pipandtansys.com &nbsp;|&nbsp; www.pipandtansys.com</footer>
  </section>

  <section class="piece envelope-back">
    <svg width="462" height="144" viewBox="0 0 462 144">
      <polyline points="0,0 231,38 462,0" fill="none" stroke="#d6d6d6" stroke-width="1"/>
    </svg>
    <div class="flap-return">14 Fernhollow Lane, Larkmoor, MN 55011</div>
    <span class="mark"></span>
    <div class="brand">Pip &amp; Tansy's</div>
  </section>

  <section class="piece envelope-front">
    <span class="mark"></span>
    <div class="brand">Pip &amp; Tansy's</div>
    <div class="tagline">clothing &amp; accessories</div>
  </section>
</body>
</html>
```